Car Soap Label Design specifically targeting RVs

I am private labeling a car wash soap to specifically target the RV industry. It will be sold in a one gallon jug with a 6"x11" spot to place the label on front and wrap around the two sides. (see attached pics for example of label size) The front of the label I want to have a realistic picture of a high dollar class A RV somehow integrated into the design, and the key features of the soap. I had wordsmithbot design a couple that I kind of like the look of that I will attach, but open to other options. I want something clean and professional looking that will back the premium product I am selling.
The name of my brand is "Blue Harbor Gleam". I want the brand name to be somewhere on the label, but not a main focus. I want the focus to be the product and its benefits. "Premium RV Wash and Wax" as the main verbiage. Benefits... "Developed for Use With Foam Gun or Bucket with Water", "Safe for All RV Exteriors", "Protective Wax Formula", "Enhanced Shine", "Water Repellent", "Streak Free Rinse", "UV Protection". On the side...Directions: 2 Ways of Mixing... Pour Concentrate into Foam Gun Bottle OR Mixing Ratio: 1 Part Wash & Wax / 3 Parts Water in bucket. Apply soap to one side of RV at a time and use carwash brush to easily loosen road film and rinse clean. On the other side... Keep from freezing, Keep Out of Reach of Children. MADE IN USA. Hazardous Ingredients: NONE . NOTICE: The seller and/or manufacturer assumes no responsibility for damage or injury resulting from misuse of this product. No warranties, expressed or implied, are given for the performance or safety of this product.

Target Market(s)

RV industry

Industry/Entity Type

RV/Auto

Requirements
Must have
• Clean, Professional look, size 6" tall and 11" wide
Nice to have
• Realistic Class A RV as part of design

```html
<!DOCTYPE html>
<html lang="en">
<head>
<meta charset="UTF-8">
<title>Premium RV Wash and Wax Label</title>
<link rel="stylesheet" href="https://fonts.googleapis.com/css2?family=Russo+One&family=Nunito+Sans:wght@400;600&display=swap">
<style>
  :root {
    --page: #ffffff;
    --navy: #1c2aa0;
    --royal: #2452cc;
    --sky: #2f9ae8;
    --band-top: #24aaf4;
    --band-bottom: #1e48c4;
    --chrome-light: #ffffff;
    --chrome-mid: #c9cdd4;
    --chrome-dark: #5f6570;
    --chrome-edge: #3a3f4a;
    --rv-white: #f3f6fb;
    --rv-grey: #b8c4d6;
    --rv-shadow: #5d6f92;
    --text-light: #eaf4ff;
  }
  * { margin: 0; padding: 0; box-sizing: border-box; }
  html, body {
    width: 1052px;
    height: 1200px;
    overflow: hidden;
    background: var(--page);
  }
  .label {
    position: absolute;
    left: 56px;
    top: 183px;
    width: 940px;
    height: 834px;
    overflow: hidden;
    background:
      radial-gradient(ellipse 52% 48% at 50% 62%, var(--sky) 0%, var(--royal) 58%, var(--navy) 100%);
  }
  .title {
    position: absolute;
    top: 72px;
    left: 0;
    width: 100%;
    text-align: center;
    font-family: "Russo One", sans-serif;
    font-weight: 400;
    text-transform: uppercase;
    filter: drop-shadow(0 3px 3px rgba(0, 0, 40, 0.65));
  }
  .title span {
    display: block;
    background: linear-gradient(180deg, var(--chrome-light) 0%, var(--chrome-mid) 42%, var(--chrome-dark) 52%, var(--chrome-mid) 78%, var(--chrome-light) 100%);
    -webkit-background-clip: text;
    background-clip: text;
    color: transparent;
    -webkit-text-stroke: 1.5px var(--chrome-edge);
  }
  .title .line-one { font-size: 90px; line-height: 80px; letter-spacing: 2px; }
  .title .line-two { font-size: 92px; line-height: 82px; letter-spacing: 1px; }
  .rv-photo {
    position: absolute;
    left: 128px;
    top: 248px;
    width: 698px;
    height: 412px;
    border-radius: 60px 120px 40px 40px;
    background:
      linear-gradient(180deg, var(--rv-white) 0%, var(--rv-white) 45%, var(--rv-grey) 72%, var(--rv-shadow) 100%);
    opacity: 0.9;
    filter: blur(14px);
  }
  .benefits {
    position: absolute;
    left: 0;
    top: 682px;
    width: 100%;
    height: 152px;
    background: linear-gradient(180deg, var(--band-top) 0%, var(--band-bottom) 100%);
    font-family: "Nunito Sans", sans-serif;
    font-weight: 600;
    font-size: 21px;
    line-height: 28px;
    color: var(--text-light);
  }
  .benefits ul {
    position: absolute;
    top: 14px;
    list-style: none;
  }
  .benefits li {
    position: relative;
    padding-left: 16px;
  }
  .benefits li::before {
    content: "";
    position: absolute;
    left: 0;
    top: 12px;
    width: 5px;
    height: 5px;
    border-radius: 50%;
    background: var(--text-light);
  }
  .benefits .col-left { left: 148px; width: 420px; }
  .benefits .col-right { left: 594px; width: 300px; }
</style>
</head>
<body>
  <main class="label">
    <h1 class="title">
      <span class="line-one">Premium RV</span>
      <span class="line-two">Wash and Wax</span>
    </h1>
    <div class="rv-photo" role="img" aria-label="Photo of a white motorhome glowing on a blue background"></div>
    <section class="benefits">
      <ul class="col-left">
        <li>Developed for Use With Foam Gun<br>or Bucket with Water</li>
        <li>Safe for All RV Exteriors</li>
        <li>Protective Wax Formula</li>
      </ul>
      <ul class="col-right">
        <li>Enhanced Shine</li>
        <li>Water Repellent</li>
        <li>Streak Free Rinse</li>
        <li>UV Protection</li>
      </ul>
    </section>
  </main>
</body>
</html>
```